Aerospace Center needs app design

We need a design that would be a creative and innovative look of a simple idea connecting air traffic control situations with sonification.
We would like to see designs that use the elements shown in the short video which are different pads, showing 4 different colors, connecting with a degree and feeling of urgency. The different pads will be movable over screen, similar as to a whiteboard where you can move things around. Each of those pads has 4 different elements that are shown:
- ATC Event (you can chose different setups)
- Select a status (you can chose between Information, Caution and Alert. Color needs to feel more alert from Information to Alert.
- Notes box (you can open the box and write additional text on it)
- Music (you can chose different files. on the right side you can see a small group of notes. When you hover over the notes, music will be played without pressing a play or stop button.
The second video is an overview of music archival program that is connected with the pads.
Look and feel
Each slider illustrates characteristics of the customer's brand and the style your logo design should communicate.

```html
<!DOCTYPE html>
<html lang="en">
<head>
<meta charset="utf-8">
<title>SONA – App Design Presentation</title>
<link rel="stylesheet" href="https://fonts.googleapis.com/css2?family=Inter:wght@400;500;600;700&family=Oswald:wght@500;600&display=swap">
<style>
:root{
  --brand:#7a6cff;
  --ink:#1f1f2e;
  --line:#ececf3;
  --page:#ffffff;
  --screen-bg:#f4f4f8;
  --green-head:#22c55e;
  --green-body:#2ecc71;
  --yellow-head:#ffd500;
  --yellow-body:#fff200;
  --red-head:#e3000e;
  --red-body:#f21d1d;
  --slate:#34495e;
  --frame:#2a2540;
}
*{box-sizing:border-box;margin:0;padding:0}
html,body{width:1200px;height:1200px;overflow:hidden;background:var(--page)}
body{font-family:"Inter",sans-serif;color:var(--ink);position:relative}
.abs{position:absolute}

.project-title{font-family:"Oswald",sans-serif;font-weight:600;font-size:18px;line-height:1;color:var(--ink);white-space:nowrap}
.project-note{font-size:12px;line-height:1;color:var(--ink);white-space:nowrap}
.spec{font-size:18px;font-weight:500}
.swatch{width:29px;height:29px;border-radius:50%;background:var(--brand)}
.hex{font-size:18px;font-weight:500;color:var(--brand)}
.notes-art{background:radial-gradient(ellipse at 30% 40%,rgba(240,120,150,.16),transparent 60%),radial-gradient(ellipse at 75% 60%,rgba(160,150,220,.16),transparent 60%)}

.nav{background:var(--brand);display:flex;align-items:center;color:#fff;position:relative;white-space:nowrap}
.brand{display:flex;align-items:center;gap:4px;font-weight:700}
.brand-dot{border-radius:50%;border:1.5px solid #fff}
.nav-item{display:flex;align-items:center;gap:3px;color:#fff}
.nav-item.active{background:#fff;color:var(--brand);border-radius:20px}
.nav-item svg{stroke:currentColor;fill:none}
.user{display:flex;align-items:center;gap:4px;margin-left:auto}
.avatar{border-radius:50%;border:1.5px solid #fff;background:linear-gradient(135deg,#c9c4e8,#7d75b5)}

.screen{position:absolute;width:510px;background:var(--screen-bg);overflow:hidden;transform-origin:0 0;border:3px solid var(--frame)}
.screen .nav{height:25px;padding:0 12px;font-size:5px}
.screen .brand{font-size:7px}
.screen .brand-dot{width:9px;height:9px}
.screen .nav-links{display:flex;gap:12px;margin-left:150px}
.screen .nav-item.active{padding:3px 6px}
.screen .avatar{width:14px;height:14px}
.searchbar{display:flex;margin:3px 13px 0;height:14px}
.searchbar .field{flex:1;background:#fff;font-size:4.5px;color:#b3b3c2;padding:4px 6px}
.searchbar .btn{width:34px;background:var(--brand);color:#fff;font-size:4.2px;font-weight:600;display:flex;align-items:center;justify-content:center;gap:2px}
.table-card{background:#fff;margin:10px 13px 0;padding-bottom:6px}
.trow{display:grid;grid-template-columns:12px 13px 30px 28px 28px 28px 25px 25px 26px 18px 30px 22px 40px 55px 44px 50px;align-items:center;font-size:4.1px;text-align:center;border-bottom:.5px solid var(--line)}
.trow>div{border-right:.5px solid var(--line);height:100%;display:flex;align-items:center;justify-content:center;line-height:1.3;overflow:hidden}
.trow>div:last-child{border-right:none}
.span2{grid-column:span 2}
.thead{height:17px;font-weight:700}
.tfilter{height:18px}
.tbody-row{height:23px;color:#4a4a5c}
.tbody-row.highlight{font-weight:700;color:var(--ink);box-shadow:0 0 0 .8px #c8c1ff,0 2px 5px rgba(122,108,255,.2);position:relative}
.mini-input{border:.5px solid #d8d8e2;height:8px;width:82%;font-size:3.4px;display:flex;align-items:center;justify-content:space-between;padding:0 2px;color:#555;white-space:nowrap}
.check{display:block;width:4px;height:4px;border:.5px solid #bbb;border-radius:1px}
.player{display:block;width:30px;height:6px;border-radius:4px;background:var(--brand);position:relative}
.player::before{content:"";position:absolute;left:3px;top:1.5px;border-left:2.5px solid #fff;border-top:1.5px solid transparent;border-bottom:1.5px solid transparent}
.player::after{content:"";position:absolute;left:8px;right:6px;top:2.7px;height:.6px;background:#fff}
.notation{display:block;width:36px;height:10px;background:linear-gradient(180deg,#fff 0,#d6d6de 50%,#fff 100%)}
.notes-box{display:block;width:38px;height:7px;border:.5px solid #d8d8e2}
.pager{display:flex;justify-content:center;gap:3px;margin-top:10px;font-size:3.5px;align-items:center}
.pager span{width:8px;height:8px;border:.5px solid #d8d8e2;display:flex;align-items:center;justify-content:center}
.pager span.on{background:var(--brand);color:#fff;border-color:var(--brand)}
.pager i{font-style:normal;color:#999}
.footnote{text-align:center;font-size:3.8px;color:#a8a8b8;margin-top:13px}

.board{position:absolute;left:75px;top:503px;width:656px;height:667px;border:7px solid var(--frame);border-radius:5px;background:#f6f6fa;overflow:hidden}
.board .nav{height:31px;padding:0 18px;font-size:5.6px}
.board .brand{font-size:8.5px}
.board .brand-dot{width:11px;height:11px}
.board .nav-item.active{padding:5px 9px}
.board .avatar{width:19px;height:19px}
.whiteboard{position:absolute;left:17px;top:42px;width:609px;height:566px;background:#fff}
.board-foot{position:absolute;left:0;right:0;top:628px;text-align:center;font-size:4.8px;color:#a8a8b8}

.zoom{position:absolute;left:111px;top:559px;width:9px;height:47px;border-radius:5px;background:var(--brand)}
.zoom::after{content:"";position:absolute;left:3px;top:18px;width:3px;height:3px;border-radius:50%;background:#fff}
.zoom-label{position:absolute;left:96px;top:579px;font-size:3.5px;color:#888;transform:rotate(-90deg)}
.caption{position:absolute;left:287px;top:613px;font-size:6.8px;font-weight:500}

.pad{position:absolute;width:123px;height:166px;overflow:hidden;box-shadow:0 10px 18px -8px rgba(0,0,0,.25)}
.pad-head{height:25px;display:flex;align-items:center;justify-content:space-between;padding:0 9px;font-size:6.8px;font-weight:600;color:#fff}
.pad-close{width:7px;height:7px;border-radius:50%;background:#fff;position:relative}
.pad-close::before,.pad-close::after{content:"";position:absolute;left:3px;top:1.5px;width:1px;height:4px;background:currentColor;transform:rotate(45deg)}
.pad-close::after{transform:rotate(-45deg)}
.pad-body{padding:6px 8px;display:flex;flex-direction:column;gap:3px}
.select{height:20px;background:#fff;display:flex;align-items:center;justify-content:space-between;padding:0 8px 0 9px;font-size:6.2px;font-weight:500;color:var(--ink)}
.select svg{width:5px;height:4px;stroke:var(--ink);fill:none;stroke-width:1.2}
.notes-btn{margin-top:3px;width:44px;height:17px;display:flex;align-items:center;gap:4px;padding-left:6px;font-size:5.4px;font-weight:500}
.notes-btn svg{width:7px;height:7px;fill:none;stroke:currentColor;stroke-width:.9}
.note-text{background:#fff;height:42px;padding:5px 7px;font-size:5px;line-height:1.6;color:#555}
.play-btn{position:absolute;right:6px;bottom:5px;width:26px;height:24px;display:flex;align-items:center;justify-content:center}
.play-btn svg{width:15px;height:15px;fill:none;stroke:#fff;stroke-width:1.1}
.hover-hint{position:absolute;right:7px;bottom:31px;font-size:3.3px;color:#fff}

.pad.green{background:var(--green-body)}
.pad.green .pad-head{background:var(--green-head)}
.pad.green .pad-close{color:var(--green-head)}
.pad.green .notes-btn{background:#fff;color:var(--ink)}
.pad.green .play-btn{border:1px solid #fff;background:rgba(255,255,255,.15)}
.pad.yellow{background:var(--yellow-body)}
.pad.yellow .pad-head{background:var(--yellow-head)}
.pad.yellow .pad-close{color:var(--yellow-head)}
.pad.yellow .notes-btn{background:#fff;color:var(--ink)}
.pad.yellow .play-btn{background:#f0b400}
.pad.red{background:var(--red-body)}
.pad.red .pad-head{background:var(--red-head)}
.pad.red .pad-close{color:var(--red-head)}
.pad.red .notes-btn{background:#fff;color:var(--ink)}
.pad.red .play-btn{border:1px solid #fff}
.pad.slate{background:#fff;border:1px solid var(--slate);border-radius:3px}
.pad.slate .pad-head{background:var(--slate)}
.pad.slate .pad-close{color:var(--slate)}
.pad.slate .select{border:1px solid #c5cad3}
.pad.slate .notes-btn{background:var(--slate);color:#fff}
.pad.slate .play-btn{background:var(--slate)}
</style>
</head>
<body>

<div class="abs project-title" style="left:82px;top:33px">01. PROJECT ONE</div>
<div class="abs project-note" style="left:213px;top:39px">[ Vertical Line&nbsp; added in table ]</div>

<!-- Archive screen A -->
<div class="screen" style="left:80px;top:87px;height:330px;transform:scale(.931)">
  <div class="nav">
    <div class="brand"><span class="brand-dot"></span>SONA</div>
    <div class="nav-links">
      <div class="nav-item active"><svg width="6" height="6" viewBox="0 0 10 10"><circle cx="5" cy="5" r="4"/></svg>Music Entries</div>
      <div class="nav-item"><svg width="6" height="6" viewBox="0 0 10 10"><path d="M2 1v8M5 1v8M8 1v8"/></svg>Music Sets</div>
      <div class="nav-item"><svg width="6" height="6" viewBox="0 0 10 10"><rect x="1" y="2" width="8" height="6"/></svg>Atc Events</div>
      <div class="nav-item"><svg width="6" height="6" viewBox="0 0 10 10"><path d="M1 6l4-4 4 4"/></svg>Help</div>
    </div>
    <div class="user"><svg width="7" height="7" viewBox="0 0 10 10" fill="none" stroke="#fff"><rect x="1" y="2" width="8" height="5"/></svg><svg width="7" height="7" viewBox="0 0 10 10" fill="none" stroke="#fff"><path d="M2 7h6L7 5V3a2 2 0 0 0-4 0v2z"/></svg><span class="avatar" role="img" aria-label="User profile photo"></span>Lena Hartwig ⌄</div>
  </div>
  <div class="searchbar"><div class="field">Search for music collections</div><div class="btn">⌕ SEARCH</div></div>
  <div class="table-card">
    <div class="trow thead"><div>Get</div><div>ID</div><div>Date</div><div>Name</div><div class="span2">Orchestration Register</div><div>Tempo</div><div>Dynamic</div><div>Complexity</div><div>Key</div><div>ATC Event</div><div>Priority</div><div>Sound File</div><div>Notation</div><div>Sets</div><div>Notes</div></div>
    <div class="trow tfilter"><div></div><div></div><div></div><div><span class="mini-input">Orin</span></div><div><span class="mini-input">piano</span></div><div><span class="mini-input">Deep ⌄</span></div><div><span class="mini-input">150</span></div><div><span class="mini-input">mf ⌄</span></div><div><span class="mini-input">1 ⌄</span></div><div><span class="mini-input">c ⌄</span></div><div><span class="mini-input">Landing ⌄</span></div><div><span class="mini-input">0 ⌄</span></div><div></div><div></div><div></div><div><span class="notes-box"></span></div></div>
    <div class="trow tbody-row"><div><span class="check"></span></div><div>01</div><div>2021-09-03</div><div>Orin<br>Suite</div><div>Piano</div><div>Deep</div><div>150</div><div>mf</div><div>1</div><div>c</div><div></div><div>0</div><div><span class="player"></span></div><div><span class="notation" role="img" aria-label="Sheet music excerpt"></span></div><div>Famous Classical<br>Motifs</div><div><span class="notes-box"></span></div></div>
    <div class="trow tbody-row"><div><span class="check"></span></div><div>02</div><div>2021-09-03</div><div>Orin<br>Suite</div><div>Piano</div><div>Deep</div><div>150</div><div>mf</div><div>1</div><div>c</div><div></div><div>0</div><div><span class="player"></span></div><div><span class="notation" role="img" aria-label="Sheet music excerpt"></span></div><div>Famous Classical<br>Motifs</div><div><span class="notes-box"></span></div></div>
    <div class="trow tbody-row highlight"><div><span class="check"></span></div><div>03</div><div>2021-09-03</div><div>Orin<br>Suite</div><div>Piano</div><div>Deep</div><div>150</div><div>mf</div><div>1</div><div>c</div><div></div><div>0</div><div><span class="player"></span></div><div><span class="notation" role="img" aria-label="Sheet music excerpt"></span></div><div>Famous Classical<br>Motifs</div><div><span class="notes-box"></span></div></div>
    <div class="trow tbody-row"><div><span class="check"></span></div><div>04</div><div>2021-09-03</div><div>Orin<br>Suite</div><div>Piano</div><div>Deep</div><div>150</div><div>mf</div><div>1</div><div>c</div><div></div><div>0</div><div><span class="player"></span></div><div><span class="notation" role="img" aria-label="Sheet music excerpt"></span></div><div>Famous Classical<br>Motifs</div><div><span class="notes-box"></span></div></div>
    <div class="trow tbody-row"><div><span class="check"></span></div><div>05</div><div>2021-09-03</div><div>Orin<br>Suite</div><div>Piano</div><div>Deep</div><div>150</div><div>mf</div><div>1</div><div>c</div><div></div><div>0</div><div><span class="player"></span></div><div><span class="notation" role="img" aria-label="Sheet music excerpt"></span></div><div>Famous Classical<br>Motifs</div><div><span class="notes-box"></span></div></div>
    <div class="trow tbody-row"><div><span class="check"></span></div><div>06</div><div>2021-09-03</div><div>Orin<br>Suite</div><div>Piano</div><div>Deep</div><div>150</div><div>mf</div><div>1</div><div>c</div><div></div><div>0</div><div><span class="player"></span></div><div><span class="notation" role="img" aria-label="Sheet music excerpt"></span></div><div>Famous Classical<br>Motifs</div><div><span class="notes-box"></span></div></div>
    <div class="trow tbody-row" style="border-bottom:none"><div><span class="check"></span></div><div>07</div><div>2021-09-03</div><div>Orin<br>Suite</div><div>Piano</div><div>Deep</div><div>150</div><div>mf</div><div>1</div><div>c</div><div></div><div>0</div><div><span class="player"></span></div><div><span class="notation" role="img" aria-label="Sheet music excerpt"></span></div><div>Famous Classical<br>Motifs</div><div><span class="notes-box"></span></div></div>
    <div class="pager"><span>1</span><span class="on">2</span><i>. . .</i><span>6</span></div>
  </div>
  <div class="footnote">Copyright © Designed &amp; Developed by sona.app 2021</div>
</div>

<!-- Archive screen B -->
<div class="screen" style="left:642px;top:69px;height:322px">
  <div class="nav">
    <div class="brand"><span class="brand-dot"></span>SONA</div>
    <div class="nav-links">
      <div class="nav-item active"><svg width="6" height="6" viewBox="0 0 10 10"><circle cx="5" cy="5" r="4"/></svg>Music Entries</div>
      <div class="nav-item"><svg width="6" height="6" viewBox="0 0 10 10"><path d="M2 1v8M5 1v8M8 1v8"/></svg>Music Sets</div>
      <div class="nav-item"><svg width="6" height="6" viewBox="0 0 10 10"><rect x="1" y="2" width="8" height="6"/></svg>Atc Events</div>
      <div class="nav-item"><svg width="6" height="6" viewBox="0 0 10 10"><path d="M1 6l4-4 4 4"/></svg>Help</div>
    </div>
    <div class="user"><svg width="7" height="7" viewBox="0 0 10 10" fill="none" stroke="#fff"><rect x="1" y="2" width="8" height="5"/></svg><svg width="7" height="7" viewBox="0 0 10 10" fill="none" stroke="#fff"><path d="M2 7h6L7 5V3a2 2 0 0 0-4 0v2z"/></svg><span class="avatar" role="img" aria-label="User profile photo"></span>Lena Hartwig ⌄</div>
  </div>
  <div class="searchbar"><div class="field">Search for music collections</div><div class="btn">⌕ SEARCH</div></div>
  <div class="table-card">
    <div class="trow thead"><div>Get</div><div>ID</div><div>Date</div><div>Name</div><div class="span2">Orchestration Register</div><div>Tempo</div><div>Dynamic</div><div>Complexity</div><div>Key</div><div>ATC Event</div><div>Priority</div><div>Sound File</div><div>Notation</div><div>Sets</div><div>Notes</div></div>
    <div class="trow tfilter"><div></div><div></div><div></div><div><span class="mini-input">Orin</span></div><div><span class="mini-input">piano</span></div><div><span class="mini-input">Deep ⌄</span></div><div><span class="mini-input">150</span></div><div><span class="mini-input">mf ⌄</span></div><div><span class="mini-input">1 ⌄</span></div><div><span class="mini-input">c ⌄</span></div><div><span class="mini-input">Landing ⌄</span></div><div><span class="mini-input">0 ⌄</span></div><div></div><div></div><div></div><div><span class="notes-box"></span></div></div>
    <div class="trow tbody-row"><div><span class="check"></span></div><div>01</div><div>2021-09-03</div><div>Orin<br>Suite</div><div>Piano</div><div>Deep</div><div>150</div><div>mf</div><div>1</div><div>c</div><div></div><div>0</div><div><span class="player"></span></div><div><span class="notation" role="img" aria-label="Sheet music excerpt"></span></div><div>Famous Classical<br>Motifs</div><div><span class="notes-box"></span></div></div>
    <div class="trow tbody-row"><div><span class="check"></span></div><div>02</div><div>2021-09-03</div><div>Orin<br>Suite</div><div>Piano</div><div>Deep</div><div>150</div><div>mf</div><div>1</div><div>c</div><div></div><div>0</div><div><span class="player"></span></div><div><span class="notation" role="img" aria-label="Sheet music excerpt"></span></div><div>Famous Classical<br>Motifs</div><div><span class="notes-box"></span></div></div>
    <div class="trow tbody-row highlight"><div><span class="check"></span></div><div>03</div><div>2021-09-03</div><div>Orin<br>Suite</div><div>Piano</div><div>Deep</div><div>150</div><div>mf</div><div>1</div><div>c</div><div></div><div>0</div><div><span class="player"></span></div><div><span class="notation" role="img" aria-label="Sheet music excerpt"></span></div><div>Famous Classical<br>Motifs</div><div><span class="notes-box"></span></div></div>
    <div class="trow tbody-row"><div><span class="check"></span></div><div>04</div><div>2021-09-03</div><div>Orin<br>Suite</div><div>Piano</div><div>Deep</div><div>150</div><div>mf</div><div>1</div><div>c</div><div></div><div>0</div><div><span class="player"></span></div><div><span class="notation" role="img" aria-label="Sheet music excerpt"></span></div><div>Famous Classical<br>Motifs</div><div><span class="notes-box"></span></div></div>
    <div class="trow tbody-row"><div><span class="check"></span></div><div>05</div><div>2021-09-03</div><div>Orin<br>Suite</div><div>Piano</div><div>Deep</div><div>150</div><div>mf</div><div>1</div><div>c</div><div></div><div>0</div><div><span class="player"></span></div><div><span class="notation" role="img" aria-label="Sheet music excerpt"></span></div><div>Famous Classical<br>Motifs</div><div><span class="notes-box"></span></div></div>
    <div class="trow tbody-row"><div><span class="check"></span></div><div>06</div><div>2021-09-03</div><div>Orin<br>Suite</div><div>Piano</div><div>Deep</div><div>150</div><div>mf</div><div>1</div><div>c</div><div></div><div>0</div><div><span class="player"></span></div><div><span class="notation" role="img" aria-label="Sheet music excerpt"></span></div><div>Famous Classical<br>Motifs</div><div><span class="notes-box"></span></div></div>
    <div class="trow tbody-row" style="border-bottom:none"><div><span class="check"></span></div><div>07</div><div>2021-09-03</div><div>Orin<br>Suite</div><div>Piano</div><div>Deep</div><div>150</div><div>mf</div><div>1</div><div>c</div><div></div><div>0</div><div><span class="player"></span></div><div><span class="notation" role="img" aria-label="Sheet music excerpt"></span></div><div>Famous Classical<br>Motifs</div><div><span class="notes-box"></span></div></div>
    <div class="pager"><span>1</span><span class="on">2</span><i>. . .</i><span>6</span></div>
  </div>
  <div class="footnote">Copyright © Designed &amp; Developed by sona.app 2021</div>
</div>

<!-- Project two description -->
<div class="abs notes-art" style="left:733px;top:665px;width:467px;height:260px" role="img" aria-label="Faint flowing musical staff with notes and treble clef"></div>
<div class="abs project-title" style="left:769px;top:528px;font-size:20px">02. PROJECT TWO</div>
<div class="abs spec" style="left:774px;top:570px">Fonts Used : Inter</div>
<div class="abs spec" style="left:771px;top:621px">Color :</div>
<div class="abs swatch" style="left:836px;top:620px"></div>
<div class="abs hex" style="left:873px;top:622px">#7a6cff</div>

<!-- Soundboard screen -->
<div class="board">
  <div class="nav">
    <div class="brand"><span class="brand-dot"></span>SONA</div>
    <div class="nav-item active" style="margin-left:44px"><svg width="8" height="7" viewBox="0 0 10 9"><rect x="1" y="1" width="8" height="7"/></svg>Soundboards ⌄</div>
    <div class="nav-item" style="margin-left:13px"><svg width="8" height="8" viewBox="0 0 10 10"><rect x="1" y="2" width="8" height="6"/></svg>Edit Soundboard ⌄</div>
    <div class="nav-item" style="margin-left:12px"><svg width="8" height="8" viewBox="0 0 10 10"><path d="M2 8V3l3-2 3 2v5z"/></svg>Surveys</div>
    <div class="nav-item" style="margin-left:10px"><svg width="10" height="8" viewBox="0 0 12 10"><path d="M1 6l5-4 5 4"/></svg>Help</div>
    <div class="nav-item" style="margin-left:104px"><svg width="9" height="9" viewBox="0 0 10 10"><circle cx="5" cy="5" r="3.5"/></svg>&nbsp;My First Experiment</div>
    <div class="user" style="gap:6px"><svg width="9" height="8" viewBox="0 0 10 10" fill="none" stroke="#fff"><rect x="1" y="2" width="8" height="5"/></svg><svg width="9" height="9" viewBox="0 0 10 10" fill="none" stroke="#fff"><path d="M2 7h6L7 5V3a2 2 0 0 0-4 0v2z"/></svg><span class="avatar" role="img" aria-label="User profile photo"></span>Lena Hartwig ⌄</div>
  </div>
  <div class="whiteboard"></div>
  <div class="board-foot">Copyright © Designed &amp; Developed by sona.app 2021</div>
</div>

<div class="zoom"></div>
<div class="zoom-label">zoom</div>
<div class="caption">When click Note button</div>

<div class="pad green" style="left:137px;top:584px">
  <div class="pad-head">Soundboard 1<span class="pad-close"></span></div>
  <div class="pad-body">
    <div class="select">Landing<svg viewBox="0 0 6 4"><path d="M1 1l2 2 2-2"/></svg></div>
    <div class="select">1.Information<svg viewBox="0 0 6 4"><path d="M1 1l2 2 2-2"/></svg></div>
    <div class="select">Orin suite<svg viewBox="0 0 6 4"><path d="M1 1l2 2 2-2"/></svg></div>
    <div class="notes-btn"><svg viewBox="0 0 10 10"><rect x="1" y="1" width="7" height="8"/><path d="M3 7l5-5"/></svg>Notes</div>
  </div>
  <div class="hover-hint">Hover to play</div>
  <div class="play-btn"><svg viewBox="0 0 16 16"><path d="M2 3h7M2 6h5M2 9h4M2 12h3M10 12V4l4-1v7"/><circle cx="9" cy="12" r="1.3"/><circle cx="13" cy="10.5" r="1.3"/></svg></div>
</div>

<div class="pad green" style="left:285px;top:629px;height:186px">
  <div class="pad-head">Soundboard 2<span class="pad-close"></span></div>
  <div class="pad-body">
    <div class="select">Landing<svg viewBox="0 0 6 4"><path d="M1 1l2 2 2-2"/></svg></div>
    <div class="select">1.Information<svg viewBox="0 0 6 4"><path d="M1 1l2 2 2-2"/></svg></div>
    <div class="select">Orin suite<svg viewBox="0 0 6 4"><path d="M1 1l2 2 2-2"/></svg></div>
    <div class="note-text" style="margin-top:4px">Lorem ipsum dolor sit amet, con-sectetur adipiscing elit, sed do eius-mod tempor incididunt ut</div>
  </div>
  <div class="play-btn"><svg viewBox="0 0 16 16"><path d="M2 3h7M2 6h5M2 9h4M2 12h3M10 12V4l4-1v7"/><circle cx="9" cy="12" r="1.3"/><circle cx="13" cy="10.5" r="1.3"/></svg></div>
</div>

<div class="pad yellow" style="left:433px;top:567px">
  <div class="pad-head">Soundboard 3<span class="pad-close"></span></div>
  <div class="pad-body">
    <div class="select">Depature<svg viewBox="0 0 6 4"><path d="M1 1l2 2 2-2"/></svg></div>
    <div class="select">2.Caution<svg viewBox="0 0 6 4"><path d="M1 1l2 2 2-2"/></svg></div>
    <div class="select">Orin suite<svg viewBox="0 0 6 4"><path d="M1 1l2 2 2-2"/></svg></div>
    <div class="notes-btn"><svg viewBox="0 0 10 10"><rect x="1" y="1" width="7" height="8"/><path d="M3 7l5-5"/></svg>Notes</div>
  </div>
  <div class="play-btn"><svg viewBox="0 0 16 16"><path d="M2 3h7M2 6h5M2 9h4M2 12h3M10 12V4l4-1v7"/><circle cx="9" cy="12" r="1.3"/><circle cx="13" cy="10.5" r="1.3"/></svg></div>
</div>

<div class="pad red" style="left:572px;top:672px">
  <div class="pad-head">Soundboard 4<span class="pad-close"></span></div>
  <div class="pad-body">
    <div class="select">Depature<svg viewBox="0 0 6 4"><path d="M1 1l2 2 2-2"/></svg></div>
    <div class="select">3.Alert<svg viewBox="0 0 6 4"><path d="M1 1l2 2 2-2"/></svg></div>
    <div class="select">Orin suite<svg viewBox="0 0 6 4"><path d="M1 1l2 2 2-2"/></svg></div>
    <div class="notes-btn"><svg viewBox="0 0 10 10"><rect x="1" y="1" width="7" height="8"/><path d="M3 7l5-5"/></svg>Notes</div>
  </div>
  <div class="play-btn"><svg viewBox="0 0 16 16"><path d="M2 3h7M2 6h5M2 9h4M2 12h3M10 12V4l4-1v7"/><circle cx="9" cy="12" r="1.3"/><circle cx="13" cy="10.5" r="1.3"/></svg></div>
</div>

<div class="pad slate" style="left:129px;top:807px">
  <div class="pad-head">Soundboard 6<span class="pad-close"></span></div>
  <div class="pad-body">
    <div class="select">Depature<svg viewBox="0 0 6 4"><path d="M1 1l2 2 2-2"/></svg></div>
    <div class="select">2.Caution<svg viewBox="0 0 6 4"><path d="M1 1l2 2 2-2"/></svg></div>
    <div class="select">Orin suite<svg viewBox="0 0 6 4"><path d="M1 1l2 2 2-2"/></svg></div>
    <div class="notes-btn"><svg viewBox="0 0 10 10"><rect x="1" y="1" width="7" height="8"/><path d="M3 7l5-5"/></svg>Notes</div>
  </div>
  <div class="play-btn"><svg viewBox="0 0 16 16"><path d="M2 3h7M2 6h5M2 9h4M2 12h3M10 12V4l4-1v7"/><circle cx="9" cy="12" r="1.3"/><circle cx="13" cy="10.5" r="1.3"/></svg></div>
</div>

<div class="pad slate" style="left:288px;top:880px">
  <div class="pad-head">Soundboard 6<span class="pad-close"></span></div>
  <div class="pad-body">
    <div class="select">Depature<svg viewBox="0 0 6 4"><path d="M1 1l2 2 2-2"/></svg></div>
    <div class="select">2.Caution<svg viewBox="0 0 6 4"><path d="M1 1l2 2 2-2"/></svg></div>
    <div class="select">Orin suite<svg viewBox="0 0 6 4"><path d="M1 1l2 2 2-2"/></svg></div>
    <div class="notes-btn"><svg viewBox="0 0 10 10"><rect x="1" y="1" width="7" height="8"/><path d="M3 7l5-5"/></svg>Notes</div>
  </div>
  <div class="play-btn"><svg viewBox="0 0 16 16"><path d="M2 3h7M2 6h5M2 9h4M2 12h3M10 12V4l4-1v7"/><circle cx="9" cy="12" r="1.3"/><circle cx="13" cy="10.5" r="1.3"/></svg></div>
</div>

<div class="pad slate" style="left:433px;top:763px">
  <div class="pad-head">Soundboard 6<span class="pad-close"></span></div>
  <div class="pad-body">
    <div class="select">Depature<svg viewBox="0 0 6 4"><path d="M1 1l2 2 2-2"/></svg></div>
    <div class="select">2.Caution<svg viewBox="0 0 6 4"><path d="M1 1l2 2 2-2"/></svg></div>
    <div class="select">Orin suite<svg viewBox="0 0 6 4"><path d="M1 1l2 2 2-2"/></svg></div>
    <div class="notes-btn"><svg viewBox="0 0 10 10"><rect x="1" y="1" width="7" height="8"/><path d="M3 7l5-5"/></svg>Notes</div>
  </div>
  <div class="play-btn"><svg viewBox="0 0 16 16"><path d="M2 3h7M2 6h5M2 9h4M2 12h3M10 12V4l4-1v7"/><circle cx="9" cy="12" r="1.3"/><circle cx="13" cy="10.5" r="1.3"/></svg></div>
</div>

<div class="pad slate" style="left:571px;top:899px">
  <div class="pad-head">Soundboard 6<span class="pad-close"></span></div>
  <div class="pad-body">
    <div class="select">Depature<svg viewBox="0 0 6 4"><path d="M1 1l2 2 2-2"/></svg></div>
    <div class="select">2.Caution<svg viewBox="0 0 6 4"><path d="M1 1l2 2 2-2"/></svg></div>
    <div class="select">Orin suite<svg viewBox="0 0 6 4"><path d="M1 1l2 2 2-2"/></svg></div>
    <div class="notes-btn"><svg viewBox="0 0 10 10"><rect x="1" y="1" width="7" height="8"/><path d="M3 7l5-5"/></svg>Notes</div>
  </div>
  <div class="play-btn"><svg viewBox="0 0 16 16"><path d="M2 3h7M2 6h5M2 9h4M2 12h3M10 12V4l4-1v7"/><circle cx="9" cy="12" r="1.3"/><circle cx="13" cy="10.5" r="1.3"/></svg></div>
</div>

</body>
</html>
```